New theatre touring show needs a high impact Hollywood style poster

Design details: We are looking for a designer to create a Poster (scalable up to A0) design for a new theatre tour. The show is based around high-octane Hollywood action films so needs to be sharp, dynamic and visually exciting.

We would like the final design supplied as a PSD so we can edit and re-size in house.

Target audience: Family audiences with children aged 8 - 15

Content:
Title - The Brightwater Stunt Magic Show
Tag Line - Get closer to the action than ever before!
Description - Join our team of special effects professionals for an interactive backstage adventure and learn the secrets of movie explosions, animatronics, and stunt sequences.

A selection of mocked up production images are enclosed which can be used or not - as you see fit.

Ideas for the visual style: Reflective of dynamic Hollywood movie posters, while being clear this is a live theatre show. We need it to feel Americanised (without using the USA flag) - think Meridale Pictures/Kestrow Pictures theme park artwork.

Things to avoid: Cartoon images

Extra notes: We have an initial concept which is enclosed for an idea of direction - please add your own elements and ideas as this is not a finished item we are looking to replicate exactly.

Theme Park

Serif
Sans Serif

0255a3
f37022

• Title - The Brightwater Stunt Magic Show
• Tag Line - Get closer to the action than ever before!
• Description - Join our team of special effects professionals for an interactive backstage adventure and learn the secrets of movie explosions, animatronics, and stunt sequences.
• Generic city scape
• Flames
• Cartoon/computer images - everything should look photographic

```html
<!DOCTYPE html>
<html lang="en">
<head>
<meta charset="utf-8">
<title>The Brightwater Stunt Magic Show</title>
<link rel="stylesheet" href="https://fonts.googleapis.com/css2?family=Marcellus&family=Marcellus+SC&display=swap">
<style>
  :root {
    --ray-orange: #f5a06c;
    --ray-white: #ffffff;
    --panel-black: #231f20;
    --text-white: #ffffff;
    --chrome-light: #ffffff;
    --chrome-mid: #b9bcc0;
    --chrome-dark: #5f6367;
  }
  * { margin: 0; padding: 0; box-sizing: border-box; }
  html, body { width: 776px; height: 1200px; overflow: hidden; }
  body { background: var(--ray-white); }

  .poster {
    position: relative;
    width: 776px;
    height: 1200px;
    overflow: hidden;
    background: repeating-conic-gradient(from 0deg at 50% 52%,
      var(--ray-orange) 0deg 5deg, var(--ray-white) 5deg 10deg);
  }

  .skyline {
    position: absolute;
    left: 0; top: 0;
    width: 776px; height: 1200px;
  }
  .skyline path { fill: var(--panel-black); }

  .title {
    position: absolute;
    left: 0; right: 0;
    top: 268px;
    text-align: center;
    font-family: "Marcellus", serif;
    text-transform: uppercase;
    line-height: 0.95;
    white-space: nowrap;
    filter: drop-shadow(1px 2px 1px rgba(0,0,0,0.8));
  }
  .title span {
    display: block;
    background: linear-gradient(180deg,
      var(--chrome-dark) 0%, var(--chrome-light) 30%, var(--chrome-mid) 48%,
      var(--chrome-dark) 55%, var(--chrome-light) 78%, var(--chrome-mid) 100%);
    -webkit-background-clip: text;
    background-clip: text;
    color: transparent;
  }
  .title .line-1 { font-size: 94px; letter-spacing: 1px; }
  .title .line-2 { font-size: 84px; letter-spacing: 2px; }
  .title .line-3 { font-size: 84px; letter-spacing: 2px; }

  .tagline {
    position: absolute;
    left: 0; right: 0;
    top: 585px;
    text-align: center;
    font-family: "Marcellus SC", serif;
    font-size: 29px;
    color: var(--text-white);
  }

  .description {
    position: absolute;
    left: 0; right: 0;
    top: 635px;
    text-align: center;
    font-family: "Marcellus SC", serif;
    font-size: 24px;
    line-height: 1.45;
    color: var(--text-white);
  }

  .gallery {
    position: absolute;
    left: 52px;
    top: 803px;
    width: 670px;
    height: 330px;
    display: flex;
    gap: 2px;
  }
  .gallery .photo { flex: 1; }
  .photo-makeup {
    background: linear-gradient(135deg, #c7b9a8 0%, #e6dcd2 45%, #8a7a6d 100%);
  }
  .photo-flames {
    background: linear-gradient(180deg, #0b0a0a 0%, #1a1210 50%, #c8501a 75%, #f7a23a 88%, #4a2210 100%);
  }
  .photo-fog {
    background: linear-gradient(160deg, #1d2a8a 0%, #3a3fd0 40%, #8a7fe0 70%, #2a2a90 100%);
  }
</style>
</head>
<body>
  <main class="poster">
    <svg class="skyline" viewBox="0 0 776 1200" aria-hidden="true">
      <path d="M35 180 H108 V35 H133 V85 H143 V85 H238 V130 H283 V130 H295 V95 L383 35 L478 95 V130 H513 V35 H625 V105 H655 V105 H740 V1160 H35 Z"/>
    </svg>

    <h1 class="title">
      <span class="line-1">Brightwater</span>
      <span class="line-2">Stunt Magic</span>
      <span class="line-3">Show</span>
    </h1>

    <p class="tagline">Get closer to the action than ever before!</p>

    <p class="description">
      Join our team of special effects professionals<br>
      for an interactive backstage adventure<br>
      and learn the secrets of movie explosions,<br>
      animatronics, and stunt sequences.
    </p>

    <div class="gallery">
      <div class="photo photo-makeup" role="img" aria-label="Production photo: make-up artist applying stage make-up to a performer"></div>
      <div class="photo photo-flames" role="img" aria-label="Production photo: performer standing among stage flames"></div>
      <div class="photo photo-fog" role="img" aria-label="Production photo: stage lighting rig in blue fog"></div>
    </div>
  </main>
</body>
</html>
```